The Bean Lantern - Looking for a stylish, cool, hipster style logo and website look and feel.

We need a logo and screen design for an e-commerce website that offers a variety of coffee blends to customers.
We first need a logo, and subsequently a theme for the entire website.
The design can be hipster/rustic/stylish, as it fits in the barrister/coffee culture environment. We are imagining a black/white logo and theme, which can also use an additional accent colour (we are open to suggestions).
In short, what we need: 1. A logo "The Bean Lantern", and a selection of fonts/accent colours for our platform.

Target Market(s)

Our target market is customers who shop coffee online. They are typically between 25 and 50 years old and value a very clean, crisp, stylish, professional design.

Industry/Entity Type

Coffee Shop

Contact Information for Business Card

logo, company name, more details to follow

Logo Text

The Bean Lantern

Number of Pages Required

1 page

Font styles to use
Sans Serif

Colors
474747
333333
000000
ffffff

Requirements
Must have
• Please note that the market we are operating in is very stylish. Some examples of the industry here:
• https://www.quillharbour.com.au/
• http://marcoandfennels.com.au/
• It is essential that our design is stylish and cool.
Nice to have
• We are looking for a very stylish, cool, minimalistic (even hipster) look and feel.
• If more text is needed for a logo, you can add:
• Australia
• Australia's best roasters
• Speciality Coffee
Should not have
• Please no brown colour (as the association with coffee).

```html
<!DOCTYPE html>
<html lang="en">
<head>
<meta charset="utf-8">
<title>The Bean Lantern — Business Card</title>
<link rel="stylesheet" href="https://fonts.googleapis.com/css2?family=Oswald:wght@500&family=Dosis:wght@400&display=swap">
<style>
  :root {
    --ink: #000000;
    --card-black: #0d0d0d;
    --paper: #ffffff;
    --paper-soft: #f2f2f2;
    --grey-mid: #474747;
    --grey-text: #9a9a9a;
    --backdrop: #e0e0e0;
  }
  * { margin: 0; padding: 0; box-sizing: border-box; }
  html, body { width: 1200px; height: 1200px; overflow: hidden; }
  body { background: var(--backdrop); position: relative; font-family: "Dosis", sans-serif; }

  .card {
    position: absolute;
    top: 494px;
    width: 347px;
    height: 214px;
    background: var(--card-black);
    color: var(--paper);
    box-shadow: 0 6px 14px rgba(0,0,0,0.12);
  }
  .card--front { left: 195px; }
  .card--back { left: 631px; display: flex; }

  /* Front */
  .front__brand {
    position: absolute;
    top: 70px; left: 0; right: 0;
    text-align: center;
    display: flex; align-items: center; justify-content: center; gap: 10px;
  }
  .brand-dot {
    width: 12px; height: 12px; border-radius: 50%;
    background: var(--paper);
  }
  .brand-name {
    font-family: "Oswald", sans-serif;
    font-weight: 500;
    font-size: 26px;
    letter-spacing: 1px;
    text-transform: uppercase;
    color: var(--paper);
  }
  .front__tagline {
    position: absolute;
    top: 176px; left: 0; right: 0;
    display: flex; align-items: center; gap: 12px;
  }
  .front__tagline::before, .front__tagline::after {
    content: ""; flex: 1; height: 1px; background: var(--paper);
  }
  .front__tagline span {
    font-family: "Oswald", sans-serif; font-weight: 500;
    font-size: 10.5px; letter-spacing: 3px; text-transform: uppercase;
  }
  .front__tagline::before { flex: 0 0 66px; }
  .front__tagline::after { flex: 1; }

  /* Back */
  .back__strip {
    width: 122px; height: 100%;
    background: var(--paper-soft);
    display: flex; flex-direction: column; align-items: center;
    padding-top: 44px;
  }
  .back__strip .brand-name {
    color: var(--ink); font-size: 13px; line-height: 1.15; text-align: center;
  }
  .back__strip .brand-dot { background: var(--ink); width: 7px; height: 7px; margin-bottom: 6px; }
  .back__info { flex: 1; position: relative; }
  .back__title {
    position: absolute; top: 108px; left: 49px; right: 0;
    font-family: "Oswald", sans-serif; font-weight: 500;
    font-size: 8.5px; letter-spacing: 2px; text-transform: uppercase;
    padding-bottom: 3px; border-bottom: 1px solid var(--paper);
  }
  .contact-list {
    position: absolute; top: 133px; left: 49px;
    list-style: none;
  }
  .contact-list li {
    display: flex; align-items: center; gap: 8px;
    height: 14px; font-size: 6.5px; color: var(--grey-text);
  }
  .contact-list svg { width: 8px; height: 8px; fill: var(--grey-text); flex: none; }
</style>
</head>
<body>
  <section class="card card--front" aria-label="Business card front">
    <div class="front__brand">
      <span class="brand-dot"></span>
      <span class="brand-name">The Bean Lantern</span>
    </div>
    <div class="front__tagline"><span>Australia's Best Roasters</span></div>
  </section>

  <section class="card card--back" aria-label="Business card back">
    <div class="back__strip">
      <span class="brand-dot"></span>
      <span class="brand-name">The Bean<br>Lantern</span>
    </div>
    <div class="back__info">
      <h2 class="back__title">The Bean Lantern</h2>
      <ul class="contact-list">
        <li><svg viewBox="0 0 10 10"><path d="M2 1h2l1 2-1.2 1a5 5 0 0 0 2.2 2.2L7 5l2 1v2c0 .6-.4 1-1 1A8 8 0 0 1 1 2c0-.6.4-1 1-1z"/></svg>02.555.0148</li>
        <li><svg viewBox="0 0 10 10"><path d="M5 0a3.5 3.5 0 0 0-3.5 3.5C1.5 6 5 10 5 10s3.5-4 3.5-6.5A3.5 3.5 0 0 0 5 0zm0 5a1.5 1.5 0 1 1 0-3 1.5 1.5 0 0 1 0 3z"/></svg>14 Wattle Lane, Kelso NSW 2795</li>
        <li><svg viewBox="0 0 10 10"><path d="M0 2h10v6H0z M.5 2.5 5 6l4.5-3.5" fill="none" stroke="#9a9a9a" stroke-width="1"/></svg>hello@thebeanlantern.com</li>
        <li><svg viewBox="0 0 10 10"><circle cx="5" cy="5" r="4.3" fill="none" stroke="#9a9a9a" stroke-width="1"/><path d="M.7 5h8.6M5 .7v8.6" stroke="#9a9a9a" stroke-width=".8"/></svg>thebeanlantern.com</li>
      </ul>
    </div>
  </section>
</body>
</html>
```